Alderpoint Web Services

This is a new It services company operating in Perth western Australia

we need a website that is easy to navigate without a cluttered feel to it it should have the following links and pages

About Us
Services
Clients
Contact Us
MY Alderpoint (login for clients)

Hi it is a web based IT services company so we would expect customers to come to the website for 2 different purposes the first is to enquire about our services and then as they become customers come to our website to manage their services so whilst they are seperate we want do not want it to look like 2 different websites

hope this helps

Hi to update this we need a home page and templates for sub pages

this is a design brief only and not the coding of the pages or building of the site

```html
<!DOCTYPE html>
<html lang="en">
<head>
<meta charset="utf-8">
<title>Alderpoint Web Services</title>
<link href="https://fonts.googleapis.com/css2?family=Open+Sans:wght@300;400;600;700&family=Arimo:wght@400;700&display=swap" rel="stylesheet">
<style>
:root{
  --brand-red:#a10d0d;
  --brand-blue:#1d9fd6;
  --heading-blue:#1a9bcf;
  --text:#555;
  --muted:#9a9a9a;
  --nav:#8a8a8a;
  --line:#e4e4e4;
  --grey-band:#f3f4f5;
  --white:#fff;
}
*{box-sizing:border-box;margin:0;padding:0}
html,body{width:835px;height:1200px;overflow:hidden;background:var(--white)}
body{font-family:"Open Sans",sans-serif;color:var(--text);position:relative}
.site-header{height:73px;display:flex;align-items:center;padding:0 112px 0 118px;justify-content:space-between}
.brand{display:flex;align-items:center;gap:8px;font-size:21px;font-weight:700;color:var(--brand-red);letter-spacing:.5px}
.brand-dot{width:38px;height:38px;border-radius:50%;background:var(--brand-red)}
.main-nav{display:flex;align-items:center;gap:26px;font-family:"Arimo",sans-serif;font-size:11px;color:var(--nav)}
.main-nav .account{background:var(--brand-red);color:var(--white);font-weight:700;padding:5px 6px;border-radius:2px}
.hero{position:relative;height:364px;background:linear-gradient(100deg,#8ea9cc 0%,#c9d5e4 22%,#eceae6 45%,#e6e2dc 70%,#cfc7bd 100%)}
.hero-copy{position:absolute;left:277px;top:52px;width:280px}
.hero-title{font-size:43px;font-weight:600;color:var(--brand-red);line-height:1}
.hero-sub{font-size:16px;font-weight:700;color:#444;margin-top:14px}
.hero-text{font-size:8.5px;line-height:13px;color:#666;margin-top:14px}
.slider-arrow{position:absolute;top:187px;width:24px;height:24px;border-radius:50%;background:rgba(120,120,120,.35)}
.slider-arrow svg{display:block}
.services{height:276px;text-align:center}
.section-title{font-size:18px;font-weight:400;color:var(--heading-blue)}
.services .section-title{padding-top:13px}
.intro{font-size:7.6px;line-height:13px;color:var(--muted);width:600px;margin:6px auto 0}
.service-list{display:flex;justify-content:center;gap:28px;margin-top:20px}
.service{width:184px}
.service-icon{width:82px;height:82px;border:1px solid #ddd;border-radius:50%;margin:0 auto;display:flex;align-items:center;justify-content:center}
.service h3{font-size:11.5px;font-weight:400;color:#555;margin-top:14px}
.service p{font-size:7.6px;line-height:14.5px;color:var(--muted);margin-top:6px}
.projects{height:287px;background:var(--grey-band);padding:17px 120px 0}
.projects-head{display:flex;justify-content:space-between;align-items:center;border-bottom:1px solid var(--line);padding-bottom:10px}
.pager{display:flex;gap:5px}
.pager span{width:13px;height:13px;border:1px solid #ccc;border-radius:50%;background:var(--white);display:flex;align-items:center;justify-content:center}
.project-list{display:flex;gap:11px;margin-top:19px}
.project{width:141px;height:188px;background:var(--white);border:1px solid #e8e8e8;padding:3px;text-align:center}
.project-media{height:102px}
.project h3{font-size:11px;font-weight:400;color:#555;margin-top:13px}
.project p{font-size:7.6px;line-height:13.6px;color:var(--muted);margin-top:5px;padding:0 6px}
.partners{height:76px;display:flex;align-items:center;justify-content:space-between;padding:0 135px 0 128px}
.partner{display:flex;align-items:center;gap:6px;font-size:15px;font-weight:600;color:#b9b9b9}
.partner i{width:22px;height:22px;border-radius:50%;background:#cfcfcf;display:block}
.contact-band{height:70px;background:var(--brand-blue);color:var(--white);text-align:center;font-family:"Arimo",sans-serif}
.contact-band h2{font-size:25px;font-weight:400;padding-top:10px}
.contact-band p{font-size:9px;margin-top:4px}
.contact-band strong{font-size:11px;font-weight:400}
.site-footer{height:54px;display:flex;align-items:center;justify-content:space-between;padding:0 115px 0 120px;font-size:7.3px;color:var(--muted)}
.social{display:flex;gap:4px;margin-left:60px}
.social span{width:15px;height:15px;border-radius:50%;background:#2f5ba8}
.social span:last-child{background:#c9302c}
.footer-nav{display:flex;gap:6px}
</style>
</head>
<body>
<header class="site-header">
  <div class="brand"><span class="brand-dot"></span>Alderpoint</div>
  <nav class="main-nav">
    <span>Home</span><span>About us</span><span>Services</span><span>Clients</span><span>Contact us</span>
    <span class="account">My Alderpoint</span>
  </nav>
</header>

<section class="hero">
  <div role="img" aria-label="Photo of a businessman in a blue shirt using a tablet" style="position:absolute;inset:0"></div>
  <div class="hero-copy">
    <h1 class="hero-title">IT SERVICES</h1>
    <p class="hero-sub">TO DELIVER BUSINESS VALUE!</p>
    <p class="hero-text">Management, Leadership and Team Building for Business Analysts and Program Managers.</p>
  </div>
  <span class="slider-arrow" style="left:45px"><svg width="24" height="24"><path d="M14 7l-5 5 5 5" fill="none" stroke="#fff" stroke-width="1.5"/></svg></span>
  <span class="slider-arrow" style="left:773px"><svg width="24" height="24"><path d="M10 7l5 5-5 5" fill="none" stroke="#fff" stroke-width="1.5"/></svg></span>
</section>

<section class="services">
  <h2 class="section-title">Our Services</h2>
  <p class="intro">Maecenas bibendum lacus gravida placerat consequat. Vivamus quis hendrerit mauris. Vestibulum laoreet felis sed consectetur sollicitudin. Sed a mauris massa. Maecenas bibendum lacus gravida placerat consequat. Vivamus quis hendrerit mauris.</p>
  <div class="service-list">
    <article class="service">
      <div class="service-icon"><svg width="30" height="32" viewBox="0 0 30 32"><rect x="3" y="1" width="14" height="28" rx="2" fill="none" stroke="#1a9bcf" stroke-width="2.5"/><rect x="7" y="8" width="5" height="2" fill="#1a9bcf"/><rect x="7" y="13" width="5" height="2" fill="#1a9bcf"/><circle cx="21" cy="16" r="5" fill="#1a9bcf"/><circle cx="21" cy="16" r="2" fill="#fff"/></svg></div>
      <h3>App Development</h3>
      <p>Nam libero tempore, cum soluta nobis est eligendi optio cumque nihil impedit quo facilis expedita distinctio minus id quod maxime placeat</p>
    </article>
    <article class="service">
      <div class="service-icon"><svg width="34" height="30" viewBox="0 0 34 30"><rect x="2" y="2" width="30" height="19" rx="1.5" fill="none" stroke="#1a9bcf" stroke-width="2.5"/><path d="M7 16l7-6 5 4 8-7" fill="none" stroke="#1a9bcf" stroke-width="1.8"/><path d="M13 21l-2 6h12l-2-6" fill="#1a9bcf"/></svg></div>
      <h3>Digital Design</h3>
      <p>Nam libero tempore, cum soluta nobis est eligendi optio cumque nihil impedit quo facilis expedita distinctio minus id quod maxime placeat</p>
    </article>
    <article class="service">
      <div class="service-icon"><svg width="34" height="34" viewBox="0 0 34 34"><g fill="#1a9bcf"><rect x="14" y="1" width="6" height="32" rx="1"/><rect x="14" y="1" width="6" height="32" rx="1" transform="rotate(45 17 17)"/><rect x="14" y="1" width="6" height="32" rx="1" transform="rotate(90 17 17)"/><rect x="14" y="1" width="6" height="32" rx="1" transform="rotate(135 17 17)"/><circle cx="17" cy="17" r="12"/></g><circle cx="17" cy="17" r="7" fill="#fff"/><circle cx="17" cy="17" r="4" fill="#1a9bcf"/></svg></div>
      <h3>Web Development</h3>
      <p>Nam libero tempore, cum soluta nobis est eligendi optio cumque nihil impedit quo facilis expedita distinctio minus id quod maxime placeat</p>
    </article>
  </div>
</section>

<section class="projects">
  <div class="projects-head">
    <h2 class="section-title">Latest Projects</h2>
    <div class="pager">
      <span><svg width="6" height="6"><path d="M4 1L2 3l2 2" fill="none" stroke="#666"/></svg></span>
      <span><svg width="6" height="6"><path d="M2 1l2 2-2 2" fill="none" stroke="#666"/></svg></span>
    </div>
  </div>
  <div class="project-list">
    <article class="project">
      <div class="project-media" role="img" aria-label="Photo of a person with a laptop on a wooden pier under a cloudy sky" style="background:linear-gradient(180deg,#bfb9b0,#7d6f66)"></div>
      <h3>Network management</h3>
      <p>Nam libero tempore, cum soluta nobis est eligendi optio cumque nihil impedit quo facilis</p>
    </article>
    <article class="project">
      <div class="project-media" role="img" aria-label="Photo of a smiling businesswoman in an office" style="background:linear-gradient(135deg,#dfe4e6,#b9b4ae)"></div>
      <h3>Internet Services</h3>
      <p>Nam libero tempore, cum soluta nobis est eligendi optio cumque nihil impedit quo facilis</p>
    </article>
    <article class="project">
      <div class="project-media" role="img" aria-label="Photo of charts on a tablet and paper beside a cup of tea" style="background:linear-gradient(135deg,#e8edf1,#c7d3dc)"></div>
      <h3>IT Solutions</h3>
      <p>Nam libero tempore, cum soluta nobis est eligendi optio cumque nihil impedit quo facilis</p>
    </article>
    <article class="project">
      <div class="project-media" role="img" aria-label="Photo of a man with a laptop and a glowing light bulb" style="background:radial-gradient(circle at 55% 40%,#4fb6c9,#12424f 70%)"></div>
      <h3>Consulting</h3>
      <p>Nam libero tempore, cum soluta nobis est eligendi optio cumque nihil impedit quo facilis</p>
    </article>
  </div>
</section>

<section class="partners">
  <span class="partner">Stackline</span>
  <span class="partner"><i></i>Orbitra</span>
  <span class="partner">Vantage</span>
  <span class="partner">Amberworks</span>
  <span class="partner"><i></i>Relayo</span>
</section>

<section class="contact-band">
  <h2>Got A Question? Get In Touch</h2>
  <p>We're here to help. Check out our FAQs, send us an email or call us at <strong>1 800 555 0142</strong></p>
</section>

<footer class="site-footer">
  <span>©2014 Alderpoint, All Rights Reserved.</span>
  <div class="social" aria-label="Social links"><span></span><span></span><span></span><span></span></div>
  <nav class="footer-nav"><span>Home</span>|<span>About</span>|<span>Services</span>|<span>Clients</span>|<span>Contacts</span></nav>
</footer>
</body>
</html>
```